Creation of a book cover
Size : 14 x 20,5 cm (+ 5 mm bleed area at the top, bottom and right areas)
The Title is a French sentence which means “The heron dreaming on the cold roof of this empty station”. It’s a surrealistic title which has no link to the story.
AUTHOR : Mathieu Vorlange
TITLE : "Le héron rêvant sur le toit froid de cette gare vide »
PUBLISHER (AT THE BOTTOM OF THE PAGE) : Editions Parvenche
I send a PDF file with the kind of cover we have imagine, but you can propose something different. The glass and the fly can of course be used.

```html
<!DOCTYPE html>
<html lang="fr">
<head>
<meta charset="UTF-8">
<title>Le héron rêvant sur le toit froid de cette gare vide — Mathieu Vorlange</title>
<link rel="stylesheet" href="https://fonts.googleapis.com/css2?family=Playfair+Display:wght@400;700;800&display=swap">
<style>
  :root {
    --backdrop: #000000;
    --paper: #faf1d9;
    --ink: #141210;
    --title-brown: #8a5433;
    --art-warm: #b59a78;
    --art-brown: #7a6148;
    --art-glass: #c4d3cd;
    --art-glass-deep: #9fb6b0;
  }
  * { margin: 0; padding: 0; box-sizing: border-box; }
  html, body {
    width: 1200px;
    height: 1200px;
    overflow: hidden;
    background: var(--backdrop);
  }
  .cover {
    position: absolute;
    left: 211px;
    top: 30px;
    width: 777px;
    height: 1139px;
    background: var(--paper);
    font-family: "Playfair Display", Georgia, serif;
  }
  .line {
    position: absolute;
    left: 0;
    width: 100%;
    text-align: center;
    white-space: nowrap;
    transform: translateY(-50%);
    line-height: 1;
  }
  .author {
    top: 106px;
    font-size: 52px;
    font-weight: 400;
    color: var(--ink);
  }
  .title { color: var(--title-brown); font-weight: 800; letter-spacing: -0.5px; }
  .title-small-a { top: 236px; font-size: 70px; }
  .title-large   { top: 320px; font-size: 94px; }
  .title-small-b { top: 409px; font-size: 70px; }
  .illustration {
    position: absolute;
    left: 241px;
    top: 535px;
    width: 357px;
    height: 410px;
  }
  .publisher {
    top: 1057px;
    font-size: 33px;
    font-weight: 400;
    letter-spacing: 3px;
    color: var(--ink);
  }
</style>
</head>
<body>
  <main class="cover">
    <p class="line author">Mathieu Vorlange</p>
    <h1>
      <span class="line title title-small-a">Le héron rêvant sur</span>
      <span class="line title title-large">le toit froid</span>
      <span class="line title title-small-b">de cette gare vide</span>
    </h1>
    <svg class="illustration" role="img" aria-label="Illustration d’une mouche posée sur le bord d’un verre d’eau, avec des bulles" viewBox="0 0 357 410">
      <defs>
        <linearGradient id="art-tone" x1="0" y1="0" x2="0" y2="1">
          <stop offset="0%" stop-color="var(--art-warm)"/>
          <stop offset="38%" stop-color="var(--art-brown)"/>
          <stop offset="58%" stop-color="var(--art-glass)"/>
          <stop offset="100%" stop-color="var(--art-glass-deep)"/>
        </linearGradient>
      </defs>
      <rect width="357" height="410" rx="18" fill="url(#art-tone)"/>
    </svg>
    <p class="line publisher">Editions Parvenche</p>
  </main>
</body>
</html>
```